Edible insect info graphic banner design

We need an info graphic that will be used to show why edible insects are so great for the environment! More pictures and less words. Preferred design would include our "superbug" and/or animated farm animals from previous design project (see attached).

Final design should have "environmental" "save the planet" feel

The winning design will include more images to describe the following points, instead if words. Size will be as per pop up banner artwork requirements in attached image (2000mm (h) x 850mm (w))

1. Include our logo

2 . Include our website CrunchyMealHall.com.au

3. Title of info graphic "why we should eat more bugs"

4. Take up little space to breed. Crates of edible insects such as crickets can be stacked on top of each other like bug apartments

5. Insects are a sustainable source of protein. High in protein, calcium, iron and amino acids, and are also low in saturated fats.

6. They taste delicious and versatile

7. 100g beef requires 2000L water, 1000g feed and creates 285g CO2.
100g cricket requires 10ml water, 90g feed and creates 0.2g CO2

8. over 80% of the world population already eats edible insects

9. by eating insects one day per week, you save over 162,000L water per year

See our website for more inspiration

Industry/Entity Type

Farm

Colors
ffffff
9bcb3c
cadf82
fbf289
faed22
33a6d7

Requirements
Must have
• Simple design, clean and clear imagery

Flexible on colours

```html
<!DOCTYPE html>
<html lang="en">
<head>
<meta charset="utf-8">
<title>Why We Should Eat More Bugs</title>
<link rel="stylesheet" href="https://fonts.googleapis.com/css2?family=Open+Sans:wght@700;800&family=Titan+One&family=Bangers&family=Noto+Serif:wght@700&display=swap">
<style>
  :root {
    --bg-top: #a9cccb;
    --bg-bottom: #8fbab9;
    --title-green: #8dc63f;
    --title-light: #cadf82;
    --cube-yellow: #faed22;
    --cube-shade: #e0d21c;
    --panel-cream: #f7ebdc;
    --ink: #333333;
    --ink-soft: #3d3d3d;
    --shadow: #1e1e1e;
    --taste-green: #c5d84a;
    --water-blue: #2a3a9e;
    --splash-blue: #33a6d7;
    --logo-olive: #7f8a2c;
    --white: #ffffff;
  }
  * { box-sizing: border-box; margin: 0; padding: 0; }
  html, body { width: 1200px; height: 2821px; overflow: hidden; }
  body {
    position: relative;
    background: linear-gradient(170deg, var(--bg-top), var(--bg-bottom));
    font-family: "Open Sans", Arial, sans-serif;
  }
  .title-band {
    position: absolute; left: 90px; top: 28px; width: 975px; height: 215px;
    background: linear-gradient(90deg, var(--title-green) 60%, var(--title-light));
    clip-path: polygon(0 8%, 100% 0, 97% 100%, 0 100%);
    display: flex; align-items: center; justify-content: center;
  }
  .title-band h1 {
    color: var(--white); font-weight: 800; font-size: 76px; line-height: 1.1;
    text-align: center; letter-spacing: 1px;
  }
  .crates { position: absolute; left: 40px; top: 470px; width: 350px; height: 355px; }
  .breed-heading {
    position: absolute; left: 262px; top: 522px;
    font-family: "Titan One", Impact, sans-serif; font-size: 44px; color: var(--white);
    text-shadow: 3px 3px 0 var(--shadow); letter-spacing: 0.5px;
  }
  .breed-text {
    position: absolute; left: 448px; top: 618px; width: 700px;
    font-weight: 800; font-size: 29px; line-height: 1.35; color: var(--ink-soft);
  }
  .protein-panel {
    position: absolute; left: 38px; top: 812px; width: 1112px; height: 575px;
    background: var(--panel-cream);
    clip-path: polygon(46% 2%, 100% 0, 100% 100%, 0 100%);
  }
  .protein-text {
    position: absolute; left: 560px; top: 835px; width: 560px;
    font-weight: 800; font-size: 25px; line-height: 1.3; color: var(--ink); text-align: center;
    transform: rotate(-3deg);
  }
  .footprint-art {
    position: absolute; left: 300px; top: 965px; width: 560px; height: 385px;
    background: linear-gradient(135deg, #d9b58a, #e8c36a 50%, #f0d0b8);
    border-radius: 24px; opacity: 0.75;
  }
  .stats {
    position: absolute; right: 62px; top: 1060px; text-align: right;
    font-family: "Noto Serif", Georgia, serif; font-weight: 700; font-size: 26px; color: var(--ink);
  }
  .stats li { list-style: none; height: 64px; }
  .taste {
    position: absolute; left: 90px; top: 1470px; width: 650px;
    font-family: "Bangers", Impact, sans-serif; font-size: 66px; line-height: 1.05;
    color: var(--taste-green); text-align: center; letter-spacing: 2px;
    text-shadow: -2px -2px 0 var(--shadow), 2px -2px 0 var(--shadow), -2px 2px 0 var(--shadow), 4px 4px 0 var(--shadow);
  }
  .dining-icon { position: absolute; left: 815px; top: 1450px; width: 230px; height: 185px; }
  .world-map {
    position: absolute; left: 150px; top: 1665px; width: 985px; height: 590px;
    background: radial-gradient(ellipse at center, rgba(255,255,255,0.85), rgba(255,255,255,0.35) 70%, rgba(255,255,255,0) 100%);
    border-radius: 40%;
  }
  .world-stat {
    position: absolute; left: 170px; top: 1812px; width: 1120px; margin-left: -130px;
    font-family: "Titan One", Impact, sans-serif; font-size: 56px; line-height: 1.3;
    color: var(--white); text-align: center; letter-spacing: 1px;
    text-shadow: 4px 4px 0 var(--shadow);
  }
  .water-splash {
    position: absolute; left: 0; top: 2150px; width: 290px; height: 320px;
    background: radial-gradient(ellipse at 40% 60%, var(--white), var(--splash-blue) 60%, rgba(51,166,215,0) 100%);
    border-radius: 50%;
  }
  .water-saving {
    position: absolute; left: 230px; top: 2330px; width: 1000px;
    font-family: "Bangers", Impact, sans-serif; font-size: 40px; line-height: 1.1;
    color: var(--water-blue); text-align: center; letter-spacing: 1.5px;
    transform: rotate(-15deg); transform-origin: center;
  }
  .brand {
    position: absolute; left: 660px; top: 2500px; display: flex; align-items: center; gap: 18px;
  }
  .brand-mark { width: 48px; height: 48px; border-radius: 50%; background: var(--logo-olive); }
  .brand-name {
    font-family: "Titan One", Impact, sans-serif; font-size: 60px; line-height: 1.0;
    color: var(--logo-olive); text-transform: uppercase;
  }
  .website {
    position: absolute; left: 235px; top: 2730px;
    font-weight: 800; font-size: 40px; color: var(--ink);
  }
</style>
</head>
<body>
  <header class="title-band"><h1>WHY WE SHOULD<br>EAT MORE BUGS</h1></header>

  <svg class="crates" viewBox="0 0 350 355" aria-hidden="true">
    <rect x="0" y="0" width="160" height="170" fill="var(--cube-yellow)"/>
    <polygon points="160,0 178,14 178,170 160,170" fill="var(--cube-shade)"/>
    <rect x="0" y="185" width="160" height="170" fill="var(--cube-yellow)"/>
    <rect x="175" y="185" width="155" height="170" fill="var(--cube-yellow)"/>
    <polygon points="330,185 348,199 348,355 330,355" fill="var(--cube-shade)"/>
    <polygon points="175,185 193,170 348,199 330,185" fill="var(--cube-shade)"/>
  </svg>
  <h2 class="breed-heading">TAKE UP LITTLE SPACE TO BREED</h2>
  <p class="breed-text">CRATES OF EDIBLE INSECTS SUCH AS CRICKETS CAN BE STACKED ON TOP OF EACH OTHER LIKE BUG APARTMENTS.</p>

  <div class="protein-panel"></div>
  <p class="protein-text">Insects are a sustainable source of protein. High in protein, calcium, iron and amino acids, and are also low in saturated fats.</p>
  <div class="footprint-art" role="img" aria-label="Feed sack arrow to farm animals labelled 1 kg, 3 kg, 5 kg and a caped superbug mascot labelled 9 kg"></div>
  <ul class="stats">
    <li>100g beef = 2000L water</li>
    <li>1000g feed = 285g CO2</li>
    <li>100g cricket =10ml water</li>
    <li>90g feed = 0.2g CO2</li>
  </ul>

  <p class="taste">THEY TASTE DELICIOUS<br>AND VERSATILE.</p>
  <svg class="dining-icon" viewBox="0 0 230 185" aria-hidden="true">
    <rect x="10" y="10" width="8" height="60" fill="#111"/>
    <rect x="24" y="10" width="8" height="60" fill="#111"/>
    <rect x="38" y="10" width="8" height="60" fill="#111"/>
    <rect x="10" y="62" width="36" height="20" rx="8" fill="#111"/>
    <rect x="22" y="80" width="12" height="100" rx="5" fill="#111"/>
    <circle cx="118" cy="98" r="72" fill="#111"/>
    <path d="M205 8 C226 40 226 90 212 100 L212 180 L198 180 L198 8 Z" fill="#111"/>
  </svg>

  <div class="world-map" role="img" aria-label="White world map silhouette"></div>
  <p class="world-stat">OVER 80% OF THE<br>WORLD POPULATION<br>ALREADY EATS<br>EDIBLE INSECTS.</p>

  <div class="water-splash" role="img" aria-label="Blue water splash"></div>
  <p class="water-saving">BY EATING INSECTS ONE DAY PER WEEK,<br>YOU SAVE OVER 162,000L WATER PER YEAR.</p>

  <div class="brand">
    <span class="brand-mark"></span>
    <span class="brand-name">Crunchy<br>Meal Hall</span>
  </div>
  <p class="website">CrunchyMealHall.com.au</p>
</body>
</html>
```